Detailing informational flyer

I want to design a new flyer for my automotive detailing business. The flyer should use the color scheme from the logo and be easy to read and understand the services we offer.

Industry/Entity Type

Automotive

Font styles to use
Serif
Sans Serif

Colors
3176b5
0255a3
fbed22
33a6d7
0692cd
ffffff

Requirements
Must have
• must include all information from the copy
Nice to have
• include a Glavenor logo such as the image attached

```html
<!DOCTYPE html>
<html lang="en">
<head>
<meta charset="utf-8">
<title>Ridgeview Carwash Detailing Center – Flyer</title>
<link href="https://fonts.googleapis.com/css2?family=Oswald:wght@300;400;500;600&family=Exo+2:wght@600;700&family=Rubik:wght@800&display=swap" rel="stylesheet">
<style>
  :root{
    --navy:#0d1f5c;
    --navy-deep:#0a1640;
    --royal:#0255a3;
    --steel:#3176b5;
    --sky:#33a6d7;
    --cyan:#0692cd;
    --pale-blue:#8fc3ef;
    --yellow:#fbed22;
    --gold:#f6d860;
    --white:#ffffff;
    --red:#c8101a;
    --red-bright:#e3121c;
    --page:#e9eaec;
  }
  *{margin:0;padding:0;box-sizing:border-box}
  html,body{width:1200px;height:934px;overflow:hidden;background:var(--page)}
  .canvas{position:relative;width:1200px;height:934px}
  .flyer{position:absolute;top:103px;width:467px;height:711px;overflow:hidden;background:var(--navy);
    box-shadow:0 10px 18px rgba(0,0,0,.25)}
  .flyer--front{left:104px}
  .flyer--back{left:617px}
  .swoosh{position:absolute;left:0;top:0;width:467px;height:711px}
  .photo{position:absolute;left:0;top:0;width:467px}
  .photo--polish{height:300px;background:radial-gradient(ellipse at 75% 55%,#c0561c 0%,#6a2a12 40%,#1f1410 80%)}
  .photo--splash{height:260px;background:linear-gradient(120deg,#3a7fcb 0%,#b3141c 35%,#d92027 55%,#1f3f86 85%)}

  .brand{position:absolute;left:0;width:467px;top:166px;display:flex;justify-content:center;align-items:center;gap:8px}
  .brand__dot{width:16px;height:16px;border-radius:50%;background:var(--yellow)}
  .brand__name{font:600 17px/1 "Oswald",sans-serif;color:var(--white);letter-spacing:1px}

  .title{position:absolute;left:0;width:467px;text-align:center;font:500 45px/50px "Oswald",sans-serif;
    color:var(--white);letter-spacing:-.5px}
  .flyer--front .title{top:246px}
  .flyer--back .title{top:40px;text-shadow:0 2px 4px rgba(0,0,0,.5)}

  .lead{position:absolute;top:350px;left:0;width:467px;text-align:center;font:600 12.5px/16px "Exo 2",sans-serif;color:var(--gold);letter-spacing:.3px}
  .services{position:absolute;top:393px;left:36px;width:396px;font:300 10.4px/13.6px "Oswald",sans-serif;color:var(--white);text-align:center}
  .services p{margin-bottom:13px}
  .services p.headlight{margin-top:26px}

  .footer{position:absolute;left:0;bottom:0;width:467px;height:40px;background:var(--red);display:flex;align-items:center;justify-content:center;
    font:600 12.5px/1 "Exo 2",sans-serif;color:var(--gold);letter-spacing:.5px}

  .savings{position:absolute;left:101px;top:217px;width:262px;height:104px;background:linear-gradient(#ffffff,#e8e8e8);border-radius:6px;
    box-shadow:0 3px 8px rgba(0,0,0,.4);text-align:center}
  .savings__label{display:block;margin-top:12px;font:500 26px/1 "Oswald",sans-serif;color:var(--navy)}
  .savings__amount{display:block;margin-top:4px;font:800 46px/1 "Rubik",sans-serif;color:var(--red-bright);letter-spacing:-1px}
  .savings__amount sup{font-size:26px;vertical-align:14px}

  .specials-label{position:absolute;left:136px;top:354px;font:500 16px/1 "Oswald",sans-serif;color:var(--yellow)}
  .pay-label{position:absolute;left:343px;top:354px;width:91px;text-align:center;font:500 15px/1 "Oswald",sans-serif;color:var(--red-bright)}
  .pay-panel{position:absolute;left:343px;top:377px;width:91px;height:276px;background:var(--white);border-radius:0 0 6px 6px}

  .specials{position:absolute;left:30px;top:380px;width:313px}
  .row{position:relative;height:67.5px;border-top:1px solid rgba(255,255,255,.55)}
  .row__type{position:absolute;left:0;top:0;width:80px;height:67px;display:flex;flex-direction:column;justify-content:center;align-items:center;
    font:500 33px/30px "Oswald",sans-serif;color:var(--sky)}
  .row__type--small span:first-child{font-size:21px;line-height:24px}
  .row__items{position:absolute;left:84px;top:6px;width:228px}
  .item{display:flex;align-items:center;height:27px}
  .item__num{width:14px;font:500 22px/27px "Oswald",sans-serif;color:var(--yellow)}
  .item__text{flex:1;font:300 9.6px/13.5px "Oswald",sans-serif;color:var(--white);white-space:nowrap;overflow:hidden}
  .item__text span{display:block}
  .item__price{width:40px;text-align:right;font:400 21px/27px "Oswald",sans-serif;color:var(--yellow)}
  .item__price sup{font-size:11px;vertical-align:9px}

  .pay-tag{position:absolute;left:354px;width:71px;height:54px;background:var(--red-bright);display:flex;align-items:center;justify-content:center;
    font:800 25px/1 "Rubik",sans-serif;color:var(--yellow);box-shadow:0 3px 4px rgba(0,0,0,.35)}
  .pay-tag sup{font-size:14px;vertical-align:9px}
</style>
</head>
<body>
<div class="canvas">

  <section class="flyer flyer--front">
    <div class="photo photo--polish" role="img" aria-label="Photo of a gloved hand polishing a car's paintwork"></div>
    <svg class="swoosh" viewBox="0 0 467 711" aria-hidden="true">
      <path d="M0,300 C110,215 280,190 467,170 L467,711 L0,711Z" fill="var(--pale-blue)"/>
      <path d="M0,330 C110,240 280,205 467,185 L467,711 L0,711Z" fill="var(--gold)"/>
      <path d="M0,352 C115,262 285,218 467,200 L467,711 L0,711Z" fill="var(--navy)"/>
    </svg>
    <div class="brand"><span class="brand__dot"></span><span class="brand__name">RIDGEVIEW CARWASH</span></div>

    <h1 class="title">RIDGEVIEW CARWASH<br>DETAILING CENTER</h1>
    <p class="lead">Ask to speak to a manager about<br>scheduling any of our detailing services.</p>

    <div class="services">
      <p>Exterior detailing includes: We wash, clay, compound, polish, and wax, as needed to restore the deep rich gloss and provide a durable shine for that “new car” look. This process removes light oxidation from the vehicle and protects the clear coat finish. Finishing touches include rim cleaning and tire shine.</p>
      <p>Interior detailing shampoo includes: We perform a deep cleaning of the interior such as the dashboard, door jams, center console, trunk area, upholstered seats, and all carpets and mats. This process will remove soils and most stains. Windows are cleaned inside and out. All leather is dressed to provide a protective finish. Air freshener is available upon request.</p>
      <p>Mini detail/ VIP service includes: Ridgeview Special Wash with triple polish wax, Glavenor Shield protectant, tire shine, and a detailed and gentle cleaning of the upholstery. 4 rubber or carpet mats are shampooed. All interior surfaces are dressed including dashboard, door panels, center console. This is followed by a detailed carpet and upholstery vacuum with compressed air to remove dirt from hard to reach places. For added shine ask about adding on our express wax service to your mini detail package.</p>
      <p class="headlight">Headlight restoration: This shop proudly offers the Headlight Service, which can polish or restore your headlight to a clear, safe condition at a fraction of the cost of headlight replacement! Restore the lens to a clear, shiny &amp; safe condition.</p>
    </div>

    <footer class="footer">48-20 Harbor Ave Elm Point &nbsp;|&nbsp; +1 555-014-2290</footer>
  </section>

  <section class="flyer flyer--back">
    <div class="photo photo--splash" role="img" aria-label="Photo of a red car being splashed with water"></div>
    <svg class="swoosh" viewBox="0 0 467 711" aria-hidden="true">
      <path d="M0,140 C120,215 300,215 467,105 L467,711 L0,711Z" fill="var(--pale-blue)"/>
      <path d="M0,160 C125,230 305,228 467,125 L467,711 L0,711Z" fill="var(--gold)"/>
      <path d="M0,172 C130,245 310,240 467,140 L467,711 L0,711Z" fill="var(--navy)"/>
    </svg>

    <h2 class="title">RIDGEVIEW CARWASH<br>DETAILING CENTER</h2>

    <div class="savings">
      <span class="savings__label">SAVE</span>
      <span class="savings__amount"><sup>$</sup>50 - <sup>$</sup>70</span>
    </div>

    <h3 class="specials-label">DETAIL SPECIALS:</h3>
    <div class="pay-label">YOU PAY ONLY</div>
    <div class="pay-panel"></div>

    <div class="specials">
      <div class="row">
        <div class="row__type"><span>CARS</span></div>
        <div class="row__items">
          <div class="item"><span class="item__num">1</span><span class="item__text"><span>Exterior detailing includes: Car wash, clay,</span><span>compound, polish, wax, and Tirelux tires</span></span><span class="item__price"><sup>$</sup>120</span></div>
          <div class="item"><span class="item__num">2</span><span class="item__text"><span>Complete Interior Shampoo. Includes: Floors,</span><span>seats, trunk, seat belts, ceiling &amp; dressing</span></span><span class="item__price"><sup>$</sup>120</span></div>
        </div>
      </div>
      <div class="row">
        <div class="row__type row__type--small"><span>MINI SUV</span><span>VANS</span></div>
        <div class="row__items">
          <div class="item"><span class="item__num">1</span><span class="item__text"><span>Exterior detailing includes: Car wash, clay,</span><span>compound, polish, wax, and Tirelux tires</span></span><span class="item__price"><sup>$</sup>135</span></div>
          <div class="item"><span class="item__num">2</span><span class="item__text"><span>Complete Interior Shampoo. Includes: Floors,</span><span>seats, trunk, seat belts, ceiling &amp; dressing</span></span><span class="item__price"><sup>$</sup>135</span></div>
        </div>
      </div>
      <div class="row">
        <div class="row__type"><span>TLC</span><span>CAR</span></div>
        <div class="row__items">
          <div class="item"><span class="item__num">1</span><span class="item__text"><span>Exterior detailing includes: Car wash, clay,</span><span>compound, polish, wax, and Tirelux tires</span></span><span class="item__price"><sup>$</sup>100</span></div>
          <div class="item"><span class="item__num">2</span><span class="item__text"><span>Complete Interior Shampoo. Includes: Floors,</span><span>seats, trunk, seat belts, ceiling &amp; dressing</span></span><span class="item__price"><sup>$</sup>110</span></div>
        </div>
      </div>
      <div class="row">
        <div class="row__type"><span>TLC</span><span>CAR</span></div>
        <div class="row__items">
          <div class="item"><span class="item__num">1</span><span class="item__text"><span>Exterior detailing includes: Car wash, clay,</span><span>compound, polish, wax, and Tirelux tires</span></span><span class="item__price"><sup>$</sup>110</span></div>
          <div class="item"><span class="item__num">2</span><span class="item__text"><span>Complete Interior Shampoo. Includes: Floors,</span><span>seats, trunk, seat belts, ceiling &amp; dressing</span></span><span class="item__price"><sup>$</sup>110</span></div>
        </div>
      </div>
    </div>

    <div class="pay-tag" style="top:393px"><sup>$</sup>175</div>
    <div class="pay-tag" style="top:459px"><sup>$</sup>195</div>
    <div class="pay-tag" style="top:527px"><sup>$</sup>145</div>
    <div class="pay-tag" style="top:594px"><sup>$</sup>165</div>

    <footer class="footer">48-20 Harbor Ave Elm Point &nbsp;|&nbsp; +1 555-014-2290</footer>
  </section>

</div>
</body>
</html>
```